Carte d'affaire bilingue

Nous avons besoin d'une carte d'affaire pour notre entreprise spécialisée en vente et achat de terrain. Nous sommes une agence immobilière et nous voulons une carte avec le recto en Français et le verso en anglais. Nous voulons une image sobre et épurée. Nous avons de la clientèle internationale et nous voulons une carte très professionnelle mais qui se démarque. Nous voulons cibler une clientèle commerciale, industrielle, contracteurs et promoteurs immobiliers.

Hi everybody, we saw all your conception and we are approching of what we like but the "WOW" is missing.

We love the little sign to specify (phone or email) but we can put them in a square to make like our logo, we love also dark gray not lite gray, we also love the stainless lines. In our logo you can see a little sign +. For us is signyfy " Always further" so if you can put many little +++++ in the conception somewhere very discret it will be appreciate. We also like a kind of round that make a magnyfying glass, because we search land we found opportunity.

Thank you

Reason: I ask different things in the last day but no one do what i am asking for. For the conception # 3016702 that we love we ask changes.

We like simplicity, urban design, corporate, international. The card must have one side in french and the other side in english. We like dark gray,silver, and a little bit of green.

Target Market(s)

Investors, developers, construction builders, etc...

Font styles to use
Serif
Sans Serif

Requirements
Must have
• logo
La mention: Agence immobilière (Francais) / Real Estate Agency (anglais)
Sous le nom: Courtier immobilier agréé (Français) / Real Estate Broker

```html
<!DOCTYPE html>
<html lang="fr">
<head>
<meta charset="utf-8">
<title>Carte d'affaire bilingue</title>
<link href="https://fonts.googleapis.com/css2?family=Cinzel:wght@500&family=Open+Sans:wght@400;600&display=swap" rel="stylesheet">
<style>
  :root {
    --backdrop: #2b2b2b;
    --card: #ffffff;
    --ink: #222222;
    --logo-gray: #5a5a5a;
    --green: #0a7a34;
    --green-dark: #0b6632;
    --green-light: #13992f;
  }
  * { box-sizing: border-box; margin: 0; padding: 0; }
  html, body { width: 1200px; height: 900px; overflow: hidden; }
  body {
    background: var(--backdrop);
    font-family: "Open Sans", Arial, sans-serif;
    position: relative;
  }
  .card {
    position: absolute;
    top: 301px;
    width: 514px;
    height: 296px;
    background: var(--card);
    box-shadow: 0 2px 8px rgba(0,0,0,.5);
    color: var(--ink);
  }
  .card--english { left: 72px; }
  .card--french { left: 615px; }

  .brand {
    position: absolute;
    left: 35px;
    top: 36px;
    display: flex;
    align-items: center;
    gap: 10px;
  }
  .brand__square {
    width: 40px;
    height: 40px;
    background: var(--green);
  }
  .brand__name {
    font-family: "Cinzel", Georgia, serif;
    font-weight: 500;
    font-size: 21px;
    line-height: 1.05;
    color: var(--logo-gray);
    letter-spacing: .5px;
  }

  .address {
    position: absolute;
    left: 330px;
    top: 40px;
    font-size: 12px;
    line-height: 18px;
  }
  .address__web { font-weight: 600; }

  .holder {
    position: absolute;
    left: 35px;
    top: 136px;
  }
  .holder__name {
    font-family: "Cinzel", Georgia, serif;
    font-weight: 500;
    font-size: 19px;
    color: var(--green);
    margin-bottom: 4px;
  }
  .holder__role { font-size: 12px; line-height: 18px; }

  .contact {
    position: absolute;
    top: 233px;
    font-size: 12px;
    line-height: 19px;
  }
  .contact--main { left: 35px; }
  .contact--extra { left: 330px; top: 236px; }
  .contact__label { color: var(--green); display: inline-block; min-width: 42px; }
  .contact--extra .contact__label { min-width: 30px; }

  .band {
    position: absolute;
    left: 0;
    bottom: 0;
    width: 514px;
    height: 22px;
    display: block;
  }
</style>
</head>
<body>

<section class="card card--english" lang="en">
  <div class="brand">
    <span class="brand__square"></span>
    <span class="brand__name">Parcel<br>Scout</span>
  </div>
  <div class="address">
    27 B, blv. Horizon, 3e<br>
    Lorvale, Qc, H0H 4K2<br>
    <span class="address__web">www.pscout.com</span>
  </div>
  <div class="holder">
    <div class="holder__name">Mireille Castonguay</div>
    <div class="holder__role">Real estate broker, D.A.<br>Vice-President</div>
  </div>
  <div class="contact contact--main">
    <div><span class="contact__label">phone:</span> 514-555-0147</div>
    <div><span class="contact__label">email:</span> m.castonguay@pscout.com</div>
  </div>
  <div class="contact contact--extra">
    <div><span class="contact__label">fax:</span> 450-555-0193</div>
    <div><span class="contact__label">free:</span> 1-866-555-0110</div>
  </div>
  <svg class="band" viewBox="0 0 514 22" aria-hidden="true">
    <polygon points="0,0 318,0 304,22 0,22" fill="var(--green-dark)"/>
    <polygon points="322,0 514,0 514,22 308,22" fill="var(--green-light)"/>
    <polygon points="318,0 322,0 308,22 304,22" fill="#ffffff"/>
  </svg>
</section>

<section class="card card--french" lang="fr">
  <div class="brand">
    <span class="brand__square"></span>
    <span class="brand__name">L'Éclaireur<br>Foncier</span>
  </div>
  <div class="address">
    27 B, boul. de l'Horizon<br>
    3e, Lorvale, Qc, H0H 4K2<br>
    <span class="address__web">www.pscout.com</span>
  </div>
  <div class="holder">
    <div class="holder__name">Mireille Castonguay</div>
    <div class="holder__role">Courtier immobilier agree, D.A.<br>Vice-Presidente</div>
  </div>
  <div class="contact contact--main">
    <div><span class="contact__label">phone:</span> 514-555-0147</div>
    <div><span class="contact__label">email:</span> m.castonguay@pscout.com</div>
  </div>
  <div class="contact contact--extra">
    <div><span class="contact__label">fax:</span> 450-555-0193</div>
    <div><span class="contact__label">free:</span> 1-866-555-0110</div>
  </div>
  <svg class="band" viewBox="0 0 514 22" aria-hidden="true">
    <polygon points="0,0 318,0 304,22 0,22" fill="var(--green-dark)"/>
    <polygon points="322,0 514,0 514,22 308,22" fill="var(--green-light)"/>
    <polygon points="318,0 322,0 308,22 304,22" fill="#ffffff"/>
  </svg>
</section>

</body>
</html>
```